Law Firm Logo and Stationary

I need a logo for my law firm.  The logo should only contain the firm name "Halvey & Halvey, P.C." but we are open to slight additions like underlining or a box.  We are looking for a modern style but not edgy because our target market is businesses and corporations.

I would like a logo that invokes the traditional values of a law firm (trust, integrity, knowledge) but I want an updated look.

To be clear, the logo should only contain the firm name, I am just looking for a font treatment.

The logo color is up to you.  The only initial opinion I have is that bright colors may not fit with the professional look of a law firm. 

I also want to incorporate the new logo into letterhead and business card designs.  The letterhead should include all of the information that is in my current letterhead, which is attached.  The letterhead should be black or grey on white.  The colored logo will go on the website and promotional materials.

For the business card, I would like to have the logo on the top left, the employee name (Colin T. Halvey) on the middle left and the firm information (address, tel, fax, website, email) on right side.  I am open to suggestions if you have better ideas.
Updates

Here are some comments on the initial 8 designs:

a) I am just interested in a font treatment of our firm name, "Halvey & Halvey, P.C."  I do not want any graphics like a gavel or shield. 

b) The full name of the firm must be in the logo.  So I cannot use designs that only have "H & H"

c) EXAMPLES: Here are two websites with examples of law firm logos that just have the firm name.  These are just samples to give you a general idea of what I am looking for.  Check out:  www.qz-legal.example and www.marrowfieldtate.example 

In short, I am looking for a simple, clean design that will look modern enough for our website but is also conservative enough to be on letterhead that gets sent to judges and other lawyers.

Also, the sample letterhead is now loaded in the brief so you can see the information I need included in the new letterhead.

Thanks.

Target Market(s)

businesses and corporations.

Industry/Entity Type

Law Firm

Logo Text

Halvey & Halvey, P.C.

Requirements
Must have
• Firm name, "Halvey & Halvey, P.C."

```html
<!DOCTYPE html>
<html lang="en">
<head>
<meta charset="utf-8">
<title>Halvey &amp; Halvey, P.C. — Identity Sheet</title>
<link href="https://fonts.googleapis.com/css2?family=Alegreya:ital,wght@0,400;1,400&display=swap" rel="stylesheet">
<style>
  :root {
    --navy: #172b45;
    --gold: #8b7616;
    --board: #201b18;
    --paper: #ffffff;
    --grey-dark: #6d6d6d;
    --grey-light: #9a9a9a;
    --grey-text: #666666;
  }
  * { margin: 0; padding: 0; box-sizing: border-box; }
  html, body { width: 741px; height: 1200px; overflow: hidden; }
  body {
    position: relative;
    background: var(--board);
    font-family: "Alegreya", Georgia, serif;
    color: var(--navy);
  }
  .logo-band {
    position: absolute; left: 0; top: 0;
    width: 741px; height: 154px;
    background: var(--paper);
  }
  .wordmark { position: absolute; white-space: nowrap; font-weight: 400; line-height: 1; }
  .wordmark--hero {
    left: 0; width: 741px; top: 46px;
    text-align: center; font-size: 54px; color: var(--navy);
  }
  .business-card {
    position: absolute; left: 223px; top: 179px;
    width: 294px; height: 168px;
    background: var(--paper); border-radius: 7px;
  }
  .wordmark--card { left: 29px; top: 21px; font-size: 17px; color: var(--navy); }
  .card-person {
    position: absolute; right: 150px; top: 84px; text-align: right;
  }
  .card-person__name { font-size: 14.5px; line-height: 1; }
  .card-person__title { font-size: 6px; font-style: italic; line-height: 1.1; }
  .card-contact {
    position: absolute; left: 159px; top: 83px;
    font-style: italic; font-size: 7.3px; line-height: 9.4px; letter-spacing: 0.25px;
  }
  .rule-pair { position: absolute; }
  .rule-pair span { display: block; }
  .rule-pair--card { left: 30px; top: 156px; width: 235px; }
  .rule-pair--card .rule-a { height: 1.3px; background: var(--gold); margin-bottom: 1.4px; }
  .rule-pair--card .rule-b { height: 1.3px; background: var(--navy); }
  .letterhead {
    position: absolute; left: 84px; top: 378px;
    width: 573px; height: 742px; background: var(--paper);
  }
  .wordmark--letterhead { left: 25px; top: 32px; font-size: 28px; color: var(--grey-dark); }
  .letterhead-footer {
    position: absolute; left: 0; width: 573px; top: 696px;
    text-align: center; font-style: italic; font-size: 7.4px;
    line-height: 10px; letter-spacing: 0.3px; color: var(--grey-text);
  }
  .rule-pair--letterhead { left: 45px; top: 719px; width: 483px; }
  .rule-pair--letterhead .rule-a { height: 2.2px; background: var(--grey-light); margin-bottom: 3px; }
  .rule-pair--letterhead .rule-b { height: 2.2px; background: var(--grey-dark); }
</style>
</head>
<body>
  <header class="logo-band">
    <div class="wordmark wordmark--hero">Halvey &amp; Halvey, P.C.</div>
  </header>

  <section class="business-card">
    <div class="wordmark wordmark--card">Halvey &amp; Halvey, P.C.</div>
    <div class="card-person">
      <div class="card-person__name">Colin T. Halvey</div>
      <div class="card-person__title">Legal Consultant</div>
    </div>
    <div class="card-contact">
      Phone: 555.014.2280<br>
      Fax: 555.014.7391<br>
      Email: colin@halvey.example<br>
      Address:<br>
      41 Larkspur Row<br>
      Suite 210<br>
      Millbrook, AL 35099
    </div>
    <div class="rule-pair rule-pair--card"><span class="rule-a"></span><span class="rule-b"></span></div>
  </section>

  <section class="letterhead">
    <div class="wordmark wordmark--letterhead">Halvey &amp; Halvey, P.C.</div>
    <div class="letterhead-footer">
      Phone: 555.014.2280, Fax: 555.014.7391, Email: colin@halvey.example<br>
      Address: 41 Larkspur Row, Suite 210, Millbrook, AL 35099
    </div>
    <div class="rule-pair rule-pair--letterhead"><span class="rule-a"></span><span class="rule-b"></span></div>
  </section>
</body>
</html>
```